velto renovation roof

We need a flyer for a new york based company called velto renovations. We are looking to promote our roofing/window/siding/concrete service.

We are a construction company with over 30 years in the business, but have set up a new company to specialize in roofing - windows - siding. We do offer general renovation service both interior (tiles, paint , Plakwall, etc) as well as concrete work (driveways, sidewalk) but we think it may be to much information for the flyer. We are fully insured and licensed

We are open to all ideas (I will include a picture of a design that caught our eye from your site).

Target Market(s)

home owners, building managers in the tri state area. We are a New York based company

Industry/Entity Type

Construction

```html
<!DOCTYPE html>
<html lang="en">
<head>
<meta charset="utf-8">
<title>Velto Renovations Flyer</title>
<link rel="stylesheet" href="https://fonts.googleapis.com/css2?family=Source+Sans+3:wght@400;600;700&display=swap">
<style>
  :root {
    --page-bg: #e9e9ea;
    --sky-top: #9fd3ea;
    --sky-glow: #e4f3fb;
    --ink: #333333;
    --brand-blue: #283a96;
    --navy: #252460;
    --white: #ffffff;
    --divider: #dbeef7;
  }
  * { box-sizing: border-box; margin: 0; padding: 0; }
  html, body {
    width: 1200px;
    height: 663px;
    overflow: hidden;
    background: var(--page-bg);
    font-family: "Source Sans 3", sans-serif;
  }
  .flyer {
    position: absolute;
    left: 23px;
    top: 59px;
    width: 1240px;
    height: 585px;
    transform: scale(0.93);
    transform-origin: 0 0;
    background: var(--divider);
  }
  .hero {
    position: absolute;
    left: 0; top: 0;
    width: 1240px; height: 222px;
    background: radial-gradient(ellipse 420px 200px at 560px 150px, var(--sky-glow), var(--sky-top) 100%);
  }
  .headline {
    position: absolute;
    left: 40px; top: 28px;
    font-size: 41px;
    line-height: 59px;
    font-weight: 400;
    color: var(--ink);
    letter-spacing: -0.2px;
  }
  .brand {
    position: absolute;
    left: 772px; top: 72px;
    color: var(--brand-blue);
    font-weight: 600;
  }
  .brand-name {
    display: block;
    font-size: 58px;
    line-height: 52px;
    letter-spacing: 12px;
  }
  .brand-tag {
    display: block;
    font-size: 42px;
    line-height: 46px;
    letter-spacing: 0.5px;
  }
  .brand-square {
    position: absolute;
    left: 1102px; top: 72px;
    width: 96px; height: 96px;
    background: var(--brand-blue);
  }
  .gallery { position: absolute; top: 222px; height: 275px; }
  .photo-house   { left: 0;   width: 440px; background: linear-gradient(180deg, #7fb2dc 0%, #b7d3ea 22%, #5e6f5c 42%, #a8957c 70%, #6e6a52 100%); }
  .photo-roofer  { left: 445px; width: 225px; background: linear-gradient(160deg, #d6dde2 0%, #8e9a7e 18%, #c8a878 40%, #6e7376 70%, #55595c 100%); }
  .photo-windows { left: 675px; width: 282px; background: linear-gradient(180deg, #d9b6ae 0%, #eadfdc 20%, #6f8c52 45%, #3f5e33 80%, #8a7868 100%); }
  .photo-siding  { left: 962px; width: 278px; background: linear-gradient(90deg, #eef0f2 0%, #b99b78 35%, #c9a783 60%, #d8dcdf 85%, #f1f2f3 100%); }
  .footer-band {
    position: absolute;
    left: 0; top: 497px;
    width: 1240px; height: 88px;
    background: var(--navy);
    color: var(--white);
  }
  .services {
    position: absolute;
    left: 28px; top: 30px;
    font-size: 24px;
    line-height: 30px;
    font-weight: 400;
    white-space: pre;
  }
  .phone {
    position: absolute;
    right: 22px; top: 24px;
    font-size: 32px;
    line-height: 38px;
    font-weight: 700;
    white-space: pre;
  }
</style>
</head>
<body>
  <div class="flyer">
    <section class="hero">
      <h1 class="headline">you get comlete service from<br>start to finish. Just call &amp; tell us...<br>WHAT YOU WANT...!</h1>
      <div class="brand">
        <span class="brand-name">VELTO</span>
        <span class="brand-tag">renovations</span>
      </div>
      <div class="brand-square"></div>
    </section>

    <div class="gallery photo-house" role="img" aria-label="Large stone and stucco house with a new green shingle roof under a blue sky"></div>
    <div class="gallery photo-roofer" role="img" aria-label="Roofer in a safety vest laying slate tiles on roof battens"></div>
    <div class="gallery photo-windows" role="img" aria-label="Two workers installing a large window frame overlooking trees"></div>
    <div class="gallery photo-siding" role="img" aria-label="Workers on ladders installing siding over sheathing on a white house"></div>

    <footer class="footer-band">
      <p class="services">Roofing | Window | Siding | General Renovation Service In The  New York  Area</p>
      <p class="phone">Call:  347-555-0148</p>
    </footer>
  </div>
</body>
</html>
```